U.S. based testing, inspection, and certification (TIC) company needs a new PowerPoint template.

We need a new PowerPoint template (deck, slide deck) for our U.S. based company with international capabilities for performing numerous testing, inspection, and certification (TIC) services. Our primary services include calibration, chemical analysis, consulting engineering, environmental simulation, forensic engineering, materials testing, mechanical testing, and nondestructive testing. Industries we serve are aerospace/aviation, automotive, chemical, commercial properties, construction, consumer products, defense, energy storage, healthcare, insurance/legal, life science, manufacturing, oil & gas, power generation, pulp & paper, and telecommunications. https://qirvotest.com/

Guideline hex colors: #29aae2, #0b1f3b, #fb6805 (use orange more subtly)

The final design should communicate:
1. Trust, Integrity, and Independence
2. Technical Expertise and Accuracy
3. Efficiency and Speed
4. Value-Added Partnership

Our current branding reflects a variety of styles, several of which have been included as attachments for reference in this project. While these examples showcase the direction we have taken in the past, we are not limited to them and remain open to exploring fresh, innovative design that is simple, clean, and with plenty of space to add content for each slide. We welcome creative concepts that build on or reimagine our existing identity to better align with our evolving vision.

```html
<!DOCTYPE html>
<html lang="en">
<head>
<meta charset="utf-8">
<title>Qirvo Technical Services — Slide Template</title>
<link rel="stylesheet" href="https://fonts.googleapis.com/css2?family=Inter:wght@400;500;600;700;800&family=JetBrains+Mono:wght@500&display=swap">
<style>
:root{
  --page:#0b1826;
  --navy:#0b1f3b;
  --navy-deep:#08172b;
  --blue:#29aae2;
  --blue-dark:#0a7fbf;
  --orange:#fb6805;
  --ink:#0b1f3b;
  --body:#33404f;
  --muted:#8592a3;
  --light:#f4f8fc;
  --line:#e3e9f0;
}
*{box-sizing:border-box;margin:0;padding:0}
html,body{width:1200px;height:1045px;overflow:hidden;background:var(--page);font-family:"Inter",sans-serif}
.canvas{position:relative;width:1200px;height:1045px}
.slide{position:absolute;width:570px;height:320px;border-radius:8px;overflow:hidden}
.slide.dark{background:radial-gradient(ellipse at 70% 10%,#0e3a63 0%,#0b2a4a 40%,#0a1c30 100%);color:#fff}
.slide.light{background:linear-gradient(160deg,#eaf5fc 0%,#ffffff 35%,#ffffff 70%,#fdf6ef 100%);color:var(--ink)}
.s1{left:24px;top:33px}.s4{left:606px;top:33px}
.s2{left:24px;top:363px}.s5{left:606px;top:363px}
.s3{left:24px;top:692px}.s6{left:606px;top:692px}
.abs{position:absolute}
.eyebrow{position:absolute;left:34px;font-size:6.5px;font-weight:600;letter-spacing:.2px;color:var(--blue-dark);text-transform:uppercase}
.eyebrow::after{content:"";display:block;width:17px;height:1px;background:var(--blue);margin-top:2px}
.dark .eyebrow{color:var(--blue)}
.title{position:absolute;left:34px;font-size:18px;font-weight:600;letter-spacing:.1px}
.footer-label{position:absolute;left:34px;bottom:10px;font-size:7px;font-weight:600;color:var(--ink)}
.footer-tags{position:absolute;left:34px;bottom:12px;font-size:5px;font-weight:600;letter-spacing:1px;color:#8ea2b8;text-transform:uppercase;display:flex;gap:5px;align-items:center}
.footer-tags i{width:3px;height:3px;border-radius:50%;background:var(--orange);display:inline-block}
.page-num{position:absolute;right:34px;bottom:10px;width:15px;height:9px;border-radius:5px;border:1px solid #d6dde6;font-size:4.5px;font-weight:600;color:var(--muted);display:flex;align-items:center;justify-content:center}
.dark .page-num{border-color:#2a4866;color:#9bb0c6;background:#0b2238}
/* slide 1 */
.brand{position:absolute;left:0;right:0;top:72px;display:flex;justify-content:center;align-items:center;gap:7px;font-size:11px;font-weight:600;color:#fff}
.brand b{width:9px;height:9px;background:#fff;display:inline-block}
.cover-title{position:absolute;left:0;right:0;top:227px;text-align:center;font-size:20.5px;font-weight:800;letter-spacing:.6px}
.cover-tag{position:absolute;left:0;right:0;top:263px;text-align:center;font-size:9.5px;color:var(--blue);letter-spacing:.3px}
/* slide 4 */
.sub{position:absolute;left:34px;top:76px;font-size:12px;font-weight:600}
.copy{position:absolute;left:34px;width:300px;font-size:8.3px;line-height:16.5px;color:var(--body)}
.photo{position:absolute}
/* slide 2 */
.cards{position:absolute;left:34px;top:91px;display:flex;gap:10px}
.card{position:relative;width:160px;height:120px;background:#fff;border-radius:4px;box-shadow:0 1px 4px rgba(11,31,59,.08);border-bottom:2px solid var(--navy);padding:13px 11px}
.card .icon{width:23px;height:23px;border-radius:4px;background:#e4f3fb;display:flex;align-items:center;justify-content:center}
.card h3{font-size:9.5px;font-weight:600;margin-top:13px}
.card p{font-size:6.2px;line-height:12.6px;color:#222c38;margin-top:10px}
.card .tag{position:absolute;right:7px;bottom:6px;font-size:3.5px;color:#a5afbb;letter-spacing:.3px}
/* slide 5 */
.chart{position:absolute;left:34px;top:123px;width:502px;height:111px;background:#fff;border-radius:5px;box-shadow:0 1px 5px rgba(11,31,59,.07);padding:13px 13px}
.row{display:flex;align-items:center;height:23.5px}
.row .label{width:92px;text-align:right;padding-right:9px;font-size:6px;font-weight:700;color:var(--ink);line-height:9px}
.track{flex:1;height:14px;background:#f3f5f8;border-radius:2px;position:relative}
.bar{height:14px;border-radius:2px;display:flex;align-items:center;justify-content:flex-end;padding-right:6px;font-size:4.6px;font-weight:700;color:#fff}
.bar.blue{background:linear-gradient(90deg,var(--navy) 0%,#0c5a8f 55%,var(--blue-dark) 100%)}
.bar.orange{background:linear-gradient(90deg,var(--navy) 0%,#6a4020 50%,var(--orange) 100%)}
.caption{position:absolute;left:0;right:0;top:243px;text-align:center;font-size:6.2px;font-style:italic;color:#3b4756}
/* slide 3 */
.s3 .copy{color:#d6e0ea;font-size:6.3px;line-height:12.8px;width:230px}
.s3 .sub{color:#fff;font-size:10.5px;top:143px}
/* slide 6 */
.close-title{position:absolute;left:0;right:0;top:205px;text-align:center;font-size:27px;font-weight:700}
.close-tag{position:absolute;left:0;right:0;top:250px;text-align:center;font-size:8.8px;color:#dbe5ee}
.pill{position:absolute;left:216px;top:273px;width:138px;height:20px;border-radius:10px;background:#0c2540;border:1px solid #24425f;display:flex;align-items:center;justify-content:center;gap:4px;font-family:"JetBrains Mono",monospace;font-size:6px;color:#e6eef5}
</style>
</head>
<body>
<main class="canvas">

  <section class="slide dark s1">
    <div class="brand"><b></b>Qirvo Technical Services</div>
    <h1 class="cover-title">QIRVO TECHNICAL SERVICES</h1>
    <p class="cover-tag">Independent Testing. Proven Accuracy.</p>
    <div class="footer-tags">Testing <i></i> Inspection <i></i> Certification</div>
    <div class="page-num">01</div>
  </section>

  <section class="slide light s4">
    <div class="eyebrow" style="top:25px">Precision Standards</div>
    <h2 class="title" style="top:38px">ISO Calibration Labs</h2>
    <h3 class="sub">Certified Signal Precision</h3>
    <p class="copy" style="top:106px">Our certified calibration laboratories isolate and correct sensor drift across dynamic electrical, thermal, and mechanical apparatus.</p>
    <p class="copy" style="top:151px">By establishing highly traceable baselines to national criteria, QTS generates absolute operational compliance across aviation, medical, and defense testing sectors.</p>
    <div class="photo" role="img" aria-label="Field engineer in hard hat and safety vest holding a tablet" style="right:10px;top:38px;width:215px;height:282px;background:linear-gradient(180deg,rgba(255,255,255,0) 0%,#e8e1c9 25%,#c9c070 60%,#b6b13c 100%);border-radius:40px 40px 0 0"></div>
    <div class="footer-label">QTS Calibration Standards</div>
    <div class="page-num">04</div>
  </section>

  <section class="slide light s2">
    <div class="eyebrow" style="top:33px">Service Divisions</div>
    <h2 class="title" style="top:46px">Core Technical Operations</h2>
    <div class="cards">
      <article class="card">
        <div class="icon"><svg width="11" height="11" viewBox="0 0 12 12"><path d="M2 1h3v1H4.5v5L2 11h8L7.5 7V2H7V1h3" fill="none" stroke="#0a7fbf" stroke-width="1.3"/></svg></div>
        <h3>Materials Testing</h3>
        <p>Advanced chemical, mechanical, and metallurgical testing protocols designed to identify microstructural stress thresholds.</p>
        <span class="tag">QTS // SYSTEM</span>
      </article>
      <article class="card">
        <div class="icon"><svg width="11" height="11" viewBox="0 0 12 12"><circle cx="5" cy="5" r="3.3" fill="none" stroke="#0a7fbf" stroke-width="1.4"/><path d="M7.5 7.5L10.5 10.5" stroke="#0a7fbf" stroke-width="1.6"/></svg></div>
        <h3>Inspection Services</h3>
        <p>Rigorous structural diagnostics and early - stage anomaly profiling across complex industrial infrastructure networks.</p>
        <span class="tag">QTS // SYSTEM</span>
      </article>
      <article class="card">
        <div class="icon"><svg width="11" height="11" viewBox="0 0 12 12"><circle cx="6" cy="6" r="4.3" fill="#0a7fbf"/></svg></div>
        <h3>Certifications</h3>
        <p>Validation sequences aligning physical materials and safety structures strictly with municipal and state codes.</p>
        <span class="tag">QTS // SYSTEM</span>
      </article>
    </div>
    <div class="footer-label">QTS Divisions</div>
    <div class="page-num">02</div>
  </section>

  <section class="slide light s5">
    <div class="eyebrow" style="top:36px">Performance Matrix</div>
    <h2 class="title" style="top:49px">Expansion Metrics by Sector</h2>
    <div class="chart">
      <div class="row"><div class="label">Calibration Services</div><div class="track"><div class="bar blue" style="width:95%">95% Growth</div></div></div>
      <div class="row"><div class="label">Materials Testing</div><div class="track"><div class="bar orange" style="width:80%">80% Capacity</div></div></div>
      <div class="row"><div class="label">Non-destructive Testing</div><div class="track"><div class="bar blue" style="width:70%">70% Capacity</div></div></div>
      <div class="row"><div class="label">Chemical Analysis</div><div class="track"><div class="bar orange" style="width:55%">55% Capacity</div></div></div>
    </div>
    <p class="caption">Visualizing optimized laboratory output capacities following strategic system expansion and sensor integration.</p>
    <div class="footer-label">QTS Capacity Metrics</div>
    <div class="page-num">05</div>
  </section>

  <section class="slide dark s3">
    <div class="eyebrow" style="top:38px">Field Capabilities</div>
    <h2 class="title" style="top:49px">Field Testing Integration</h2>
    <h3 class="sub">Resolving Obstacles On - Site</h3>
    <p class="copy" style="top:165px">Directly drawing from operational themes in, QTS delivers localized diagnostic support to resolve deep structural and material stresses directly in the field.<br>Our rapid - response audits integrate cleanly into active operational environments, validating mechanical assets and turbine structures against rigorous flight and safety criteria.</p>
    <div class="photo" role="img" aria-label="Technician servicing an aircraft piston engine in a hangar" style="left:296px;top:121px;width:240px;height:137px;border-radius:4px;background:linear-gradient(135deg,#8a8f94 0%,#6d5246 40%,#3e4a5c 75%,#2a3340 100%)"></div>
    <div class="footer-tags">QTS <i></i> Aerospace Auditing</div>
    <div class="page-num">03</div>
  </section>

  <section class="slide dark s6">
    <h2 class="close-title">Technical Partnership</h2>
    <p class="close-tag">Providing the diagnostic clarity your high-consequence operations require.</p>
    <div class="pill"><svg width="6" height="6" viewBox="0 0 10 10"><circle cx="5" cy="5" r="4.5" fill="#29aae2"/></svg>qirvotest.com | Lakemont, Ohio</div>
    <div class="footer-tags">Testing <i></i> Inspection <i></i> Certification</div>
    <div class="page-num">06</div>
  </section>

</main>
</body>
</html>
```